Buch-/E-Book-Cover für Ausbildung und Weiterbildung von angehenden Sommeliers und Connaisseurs in der Spirituosenbranche
Zielgruppe
Ausbildung und Weiterbildung von angehenden Sommeliers und Connaisseurs in der Spirituosenbranche. Zielgruppe sind die Teilnehmer der genannten Kurse, Interessierte, Brenner und Gastronomen.
Aufgabenstellung
Klassisches, edles Design, klares Design, keine Bilder, Typografie steht im Vordergrund. Typografie in Relief.
A4
Vom Stil wie die angehängte Datei
Buchtitel: Kernwasser (groß) - verschnörkelt -
Hintergrund - Blautöne
Schrift: Titel Silber Untertitel: grau
Unterüberschrift: Kultur und Genuss
Autoren: Lehmkuhl • Wittrock
Buchrücken: Oben: Lehmkuhl Wittrock - Quer: Kernwasser - Unten: Amber Vessels

```html
<!DOCTYPE html>
<html lang="de">
<head>
<meta charset="utf-8">
<title>Kernwasser – Kultur und Genuss</title>
<link rel="stylesheet" href="https://fonts.googleapis.com/css2?family=Kaushan+Script&family=Nunito+Sans:wght@300;400&display=swap">
<style>
  :root {
    --cover-blue: #044f84;
    --spine-rule: #0b0b0b;
    --title-silver: #cdcdcd;
    --text-grey: #9b9b9b;
  }
  html, body {
    margin: 0;
    padding: 0;
    width: 980px;
    height: 1200px;
    overflow: hidden;
    background: var(--cover-blue);
  }
  .cover {
    position: relative;
    width: 980px;
    height: 1200px;
    background: var(--cover-blue);
    font-family: "Nunito Sans", "Avenir Next", sans-serif;
    font-weight: 300;
    color: var(--text-grey);
  }
  .spine {
    position: absolute;
    left: 0;
    top: 0;
    width: 126px;
    height: 1200px;
  }
  .spine-rule {
    position: absolute;
    left: 126px;
    top: 0;
    width: 4px;
    height: 1200px;
    background: var(--spine-rule);
  }
  .spine-authors,
  .spine-publisher {
    position: absolute;
    left: 0;
    width: 126px;
    text-align: center;
    font-size: 25px;
    line-height: 37px;
    margin: 0;
  }
  .spine-authors { top: 20px; }
  .spine-publisher { top: 1104px; font-size: 23px; }
  .spine-title {
    position: absolute;
    left: 63px;
    top: 575px;
    transform: translate(-50%, -50%) rotate(-90deg);
    white-space: nowrap;
    font-family: "Kaushan Script", cursive;
    font-size: 72px;
    line-height: 1;
    color: var(--title-silver);
    margin: 0;
  }
  .front {
    position: absolute;
    left: 130px;
    top: 0;
    width: 850px;
    height: 1200px;
  }
  .book-title {
    position: absolute;
    left: 0;
    width: 850px;
    top: 392px;
    margin: 0;
    text-align: center;
    font-family: "Kaushan Script", cursive;
    font-weight: 400;
    font-size: 128px;
    line-height: 1.2;
    color: var(--title-silver);
  }
  .book-subtitle {
    position: absolute;
    left: 0;
    width: 850px;
    top: 584px;
    margin: 0;
    text-align: center;
    font-size: 70px;
    font-weight: 300;
    line-height: 1.2;
    letter-spacing: 1px;
  }
  .book-authors {
    position: absolute;
    left: 0;
    width: 850px;
    top: 1105px;
    margin: 0;
    text-align: center;
    font-size: 48px;
    line-height: 1.2;
  }
  .author-dot {
    display: inline-block;
    width: 17px;
    height: 17px;
    border-radius: 50%;
    background: var(--text-grey);
    vertical-align: middle;
    margin: 0 16px;
    position: relative;
    top: -4px;
  }
</style>
</head>
<body>
  <div class="cover">
    <aside class="spine">
      <p class="spine-authors">Lehmkuhl<br>Wittrock</p>
      <p class="spine-title">Kernwasser</p>
      <p class="spine-publisher">Amber<br>Vessels</p>
    </aside>
    <div class="spine-rule"></div>
    <main class="front">
      <h1 class="book-title">Kernwasser</h1>
      <h2 class="book-subtitle">Kultur und Genuss</h2>
      <p class="book-authors">Lehmkuhl<span class="author-dot"></span>Wittrock</p>
    </main>
  </div>
</body>
</html>
```